Fitness Equipment Repair Business Needs a Catchy New Business Card

We have an existing business card, however, it is quite plain and boring. We are expanding primarily in the commercial area (gyms, studios, apartment complexes etc). The business card will serve as eye candy to those managers/owners that can't be met for a face to face.
Originally I was planning for a brochure as well, but all of our information is better summarized on our website. (brookmotionservice.ca).
I would like the card to match the colour scheme of the website and utilize the logo. It should have a professional clean feel to it, however, a little colouring outside the lines wouldn't hurt.
The example card is for my service technician (Colin Harstad). If possible I would like to be able to edit the text to use for more than one person.

Industry/Entity Type

Appliance Repair

Contact Information for Business Card

Clean, crisp and professional but needs to be eye catching. Preferably using the black, white and red colour scheme matching the website. Double sided would be nice, but is not necessary.

Colors
ec1f27
ffffff
000000

Requirements
Must have
• Must be able to edit name, phone number and title to use for multiple people. Must show the company website (brookmotionservice.ca).

```html
<!DOCTYPE html>
<html lang="en">
<head>
<meta charset="utf-8">
<title>Brook Motion Service – Business Card</title>
<link rel="stylesheet" href="https://fonts.googleapis.com/css2?family=Marcellus+SC&family=PT+Sans:wght@400;700&display=swap">
<style>
  :root {
    --brand-red: #ec1f27;
    --brand-black: #000000;
    --brand-white: #ffffff;
    --ink-grey: #4a4a4a;
    --backdrop: #e9e6e2;
    --circle-tint: #d91a22;
  }
  * { margin: 0; padding: 0; box-sizing: border-box; }
  html, body { width: 1200px; height: 987px; overflow: hidden; background: var(--backdrop); }
  .canvas { position: relative; width: 1200px; height: 987px; }

  .card {
    position: absolute;
    left: 293px;
    width: 615px;
    height: 352px;
    overflow: hidden;
    box-shadow: 0 2px 6px rgba(0,0,0,.25);
  }
  .card--front { top: 130px; background: var(--brand-white); }
  .card--back  { top: 506px; background: var(--brand-red); }

  /* Front */
  .front-header {
    position: absolute; left: 0; top: 0; width: 100%; height: 190px;
    background: var(--brand-black);
    border-bottom: 4px solid var(--brand-red);
  }
  .brand-mark {
    position: absolute; left: 130px; top: 58px;
    width: 70px; height: 70px; border-radius: 50%;
    background: var(--brand-red);
  }
  .brand-name {
    position: absolute; left: 223px; top: 78px;
    font-family: "Marcellus SC", serif;
    font-size: 22px; color: var(--brand-white); letter-spacing: .5px;
    white-space: nowrap;
  }
  .identity {
    position: absolute; right: 340px; top: 222px;
    text-align: right;
    font-family: "PT Sans", sans-serif;
  }
  .identity .person-name {
    font-family: "Marcellus SC", serif;
    font-size: 23px; line-height: 26px; color: var(--brand-red); font-weight: 400;
    letter-spacing: .5px; white-space: nowrap;
  }
  .identity .person-title {
    font-family: "Marcellus SC", serif;
    font-size: 17px; line-height: 22px; color: var(--ink-grey); letter-spacing: .5px;
  }
  .identity .address { margin-top: 2px; font-size: 16px; line-height: 23px; color: var(--ink-grey); }

  .contact-list {
    position: absolute; left: 305px; top: 225px; list-style: none;
    font-family: "PT Sans", sans-serif; font-size: 16px; line-height: 23px; color: var(--ink-grey);
  }
  .contact-list li { display: flex; align-items: center; gap: 7px; white-space: nowrap; }
  .contact-list svg { width: 13px; height: 13px; flex: none; }

  /* Back */
  .back-emblem {
    position: absolute; left: 380px; top: 80px;
    width: 340px; height: 340px; border-radius: 50%;
    background: var(--circle-tint);
  }
  .back-brand {
    position: absolute; left: 38px; top: 278px;
    font-family: "Marcellus SC", serif; font-size: 25px; line-height: 28px;
    color: var(--brand-white); letter-spacing: .5px; white-space: nowrap;
  }
  .back-web {
    position: absolute; left: 38px; top: 308px;
    font-family: "PT Sans", sans-serif; font-size: 15px;
    color: var(--brand-white); letter-spacing: 2.4px;
  }
</style>
</head>
<body>
<main class="canvas">

  <section class="card card--front" aria-label="Business card front">
    <header class="front-header">
      <span class="brand-mark" aria-hidden="true"></span>
      <p class="brand-name">Brook Motion Service</p>
    </header>

    <div class="identity">
      <p class="person-name">Colin Harstad</p>
      <p class="person-title">Service technician</p>
      <p class="address">1875 Larch Cres NW<br>Edmonton AB T6R 0K4</p>
    </div>

    <ul class="contact-list">
      <li>
        <svg viewBox="0 0 16 16" aria-hidden="true"><path fill="#ec1f27" d="M3.6 1.2l2.3 2.6-1.2 2a8.8 8.8 0 0 0 5.5 5.5l2-1.2 2.6 2.3-1.3 2.4C7.1 14.6 1.4 8.9 1.2 2.5z"/></svg>
        587-555-0142(Personal)
      </li>
      <li>
        <svg viewBox="0 0 16 16" aria-hidden="true"><path fill="#ec1f27" d="M3.6 1.2l2.3 2.6-1.2 2a8.8 8.8 0 0 0 5.5 5.5l2-1.2 2.6 2.3-1.3 2.4C7.1 14.6 1.4 8.9 1.2 2.5z"/></svg>
        780-555-0187(Service Line)
      </li>
      <li>
        <svg viewBox="0 0 16 16" aria-hidden="true"><rect x="1" y="3.5" width="14" height="9" fill="#ec1f27"/><path d="M1.5 4l6.5 5 6.5-5" fill="none" stroke="#fff" stroke-width="1.2"/></svg>
        info@brookmotion.ca
      </li>
      <li>
        <svg viewBox="0 0 16 16" aria-hidden="true"><circle cx="8" cy="8" r="6.5" fill="#ec1f27"/><path d="M1.5 8h13M8 1.5c-3 3.5-3 9.5 0 13M8 1.5c3 3.5 3 9.5 0 13" fill="none" stroke="#fff" stroke-width="1"/></svg>
        www.brookmotionservice.ca
      </li>
    </ul>
  </section>

  <section class="card card--back" aria-label="Business card back">
    <span class="back-emblem" aria-hidden="true"></span>
    <p class="back-brand">Brook Motion Service</p>
    <p class="back-web">www.brookmotionservice.ca</p>
  </section>

</main>
</body>
</html>
```